Agricultural and Earthmoving business card design

We need a business card design for a new company based in Kilmore, Victoria. We are a versatile company with two specialties, the first is an earthworks side, we do big and small jobs, from soccer fields for councils and football clubs down to house cuts for the public, horse ridding arena's, tennis courts and drainage are also small jobs we have experience in. Not only do we do earthmoving, but we also have a lot of experience in the agricultural side of machinery work, from pasture improvements to a lot of experience in hay contracting. We need a business card that doesn't focus on only one side of our business but blends both skills. We would like a primarily black business card that incorporates our company logo. Our company colours are black red , grey and white.

Industry/Entity Type

House

Contact Information for Business Card

Brantwell Contracting, Neil Brantwell, 2716 Easton Hwy Wendale Vic 3758, Phone: 03 5924 6308, Mobile: 0427 913 084. Specialising in Earthmoving, synthetic and natural turf, landscaping, drainage. Also specialising in Agricultural improvements and hay contracting.

Requirements
Must have
• A good blend of both earthmoving and agricultural contracting. Company logo.

```html
<!DOCTYPE html>
<html lang="en">
<head>
<meta charset="utf-8">
<title>Brantwell Contracting – Business Card</title>
<link rel="stylesheet" href="https://fonts.googleapis.com/css2?family=Arimo:wght@400;700&family=Cabin:wght@600;700&display=swap">
<style>
  :root {
    --card-black: #000000;
    --frame-red: #d0021b;
    --title-red: #e30613;
    --ink: #111111;
    --panel-light: #f2f2f2;
    --panel-mid: #dcdcdc;
    --panel-dark: #c4c4c4;
    --art-soil: #5b5048;
    --art-body: #2b2b2b;
  }
  html, body {
    margin: 0;
    padding: 0;
    width: 1200px;
    height: 741px;
    overflow: hidden;
    background: var(--card-black);
  }
  .card {
    position: relative;
    width: 1200px;
    height: 741px;
    background: var(--card-black);
    font-family: "Arimo", Arial, sans-serif;
    color: var(--ink);
  }
  .card-frame {
    position: absolute;
    left: 16px; top: 16px;
    width: 1160px; height: 700px;
    border: 4px solid var(--frame-red);
  }
  .card-panel {
    position: absolute;
    left: 41px; top: 41px;
    width: 1111px; height: 653px;
    background: linear-gradient(90deg, var(--panel-mid) 0%, var(--panel-light) 30%, var(--panel-light) 60%, var(--panel-mid) 85%, var(--panel-dark) 100%);
  }
  .logo-art {
    position: absolute;
    left: 151px; top: 63px;
    width: 265px; height: 145px;
  }
  .company-name {
    position: absolute;
    left: 435px; top: 55px;
    width: 680px;
    margin: 0;
    text-align: center;
    font-family: "Arimo", Arial, sans-serif;
    font-weight: 700;
    font-variant: small-caps;
    font-size: 61px;
    line-height: 1;
    color: var(--title-red);
  }
  .owner-name {
    position: absolute;
    left: 695px; top: 132px;
    width: 400px;
    margin: 0;
    text-align: center;
    font-family: "Cabin", "Trebuchet MS", sans-serif;
    font-weight: 700;
    font-size: 44px;
    line-height: 1;
  }
  .specialties {
    position: absolute;
    left: 41px; top: 228px;
    width: 1111px;
    margin: 0;
    text-align: center;
    font-family: "Cabin", "Trebuchet MS", sans-serif;
    font-weight: 700;
    font-size: 30px;
    line-height: 39px;
  }
  .job-list {
    position: absolute;
    left: 78px; top: 356px;
    margin: 0;
    padding: 0 0 0 25px;
    font-size: 26px;
    line-height: 38px;
  }
  .job-list strong { font-weight: 700; font-size: 28px; }
  .agri-note {
    position: absolute;
    right: 72px; top: 354px;
    margin: 0;
    text-align: right;
    font-size: 26px;
    line-height: 38px;
  }
  .contact-phones {
    position: absolute;
    left: 73px; top: 594px;
    margin: 0;
    font-weight: 700;
    font-size: 35px;
    line-height: 44px;
  }
  .contact-address {
    position: absolute;
    left: 640px; top: 600px;
    width: 500px;
    margin: 0;
    text-align: center;
    font-size: 34px;
    line-height: 44px;
  }
</style>
</head>
<body>
<main class="card">
  <div class="card-frame"></div>
  <div class="card-panel"></div>

  <svg class="logo-art" viewBox="0 0 265 145" role="img" aria-label="Illustration of a loaded dump truck carrying soil">
    <defs>
      <linearGradient id="truckTone" x1="0" y1="0" x2="0" y2="1">
        <stop offset="0" stop-color="#6e635a"/>
        <stop offset="0.6" stop-color="var(--art-body)"/>
        <stop offset="1" stop-color="#4a4038"/>
      </linearGradient>
    </defs>
    <rect x="0" y="0" width="265" height="145" rx="10" fill="url(#truckTone)"/>
  </svg>

  <h1 class="company-name">Brantwell Contracting</h1>
  <p class="owner-name">Neil Brantwell</p>

  <p class="specialties">
    Specialising in Earthmoving, synthetic and natural turf, landscaping &amp; drainage<br>
    Also specialising in Agricultural improvements and hay contracting
  </p>

  <ul class="job-list">
    <li><strong>BIG</strong> and small jobs</li>
    <li>Soccer fields for councils and football clubs</li>
    <li>House cuts for the public</li>
    <li>Horse riding arenas</li>
    <li>Tennis courts and drainage</li>
  </ul>

  <p class="agri-note">
    Not only do we do earthmoving...<br>
    we also have a lot of experience in<br>
    the agricultural side of machinery work,<br>
    from pasture improvements<br>
    to a lot of experience in hay contracting.
  </p>

  <p class="contact-phones">
    Phone: 03 5924 6308<br>
    Mobile: 0427 913 084
  </p>

  <p class="contact-address">
    Address: 2716 Easton Hwy<br>
    Wendale Vic 3758
  </p>
</main>
</body>
</html>
```